Medical Internet Marketing Company Needs a Site!

We need a new, fresh website for our search engine optimization and social media marketing company. We specialize in helping medical practices, doctors, physicians, and hospitals with their online presence and web ranking. The site should lean towards being suited for these audiences.

We have several examples of website that we like as well as things that we like about them.

Here are sites that we enjoy.

www.brightwavepromo.com

It's a good design for the site all around. The videos, buttons, and images are all excellent. They did a fine job.

- We really like their "contact us" side bar and want to include one like it on the secondary pages.

www.kestrelgrow.net

- We don't like the "thickness" of the top navigation bar.
- We like the page colors, easy navigation, and big call to action phone number in the top right corner.

http://www.tulavo.com/

Out of all the examples provided, Tulavo is our favorite and closest look and style to what we are looking for.

- We really like the openness of the design, such as space between the text and background.

- We want a price page in a style very similar to their pricing page with the services listed and check-marks, etc. although we intend to have multiple service package columns much like Kestrel's SEO pricing page.

- The way the video fits into the home page header is very organized, simple, and attention grabbing. We intend to place a slider with videos here.

- We need a page design that will allow for an image slider like Tulavo's Features page.

Here's a great example of a medical internet marketing website: http://www.dorvanta.com/

Target Market(s)

Our target market is doctors, typically male and typically 40-45 years old. I

Industry/Entity Type

Marketing

Requirements
Must have
• The homepage should have a slider in the video. Interior pages should have a video in the very top similar to how they do it on www.brightwavepromo.com

The top navigation tabs needed are:
- Home
- Solutions
- Resources
- About
- Why Zentrol
- Contact

The sidebar should have a GREAT call to action in it on interior pages.

There should be one interior page that is similar to this - http://www.tulavo.com/pricing/

There needs to be a page with multiple boxes that take up a row of the web page's body. This page will house all the case studies similar to brightwave promo's: http://www.brightwavepromo.com/success-stories/case-studies/ The one exception is we want the case studies to be inside of "boxes" instead of between horizontal lines like brightwave promo's.
Nice to have
• Color, professional, and clean. GREAT use of calls to actions.

```html
<!DOCTYPE html>
<html lang="en">
<head>
<meta charset="utf-8">
<title>Zentrol – Internet Marketing for Medical Practices</title>
<link href="https://fonts.googleapis.com/css2?family=Arimo:wght@400;700&family=Oswald:wght@500&display=swap" rel="stylesheet">
<style>
:root{
  --blue:#1f9ad8;
  --blue-dark:#1787c4;
  --nav-top:#5cc3ef;
  --nav-bottom:#2a9fd9;
  --gold:#e7b23a;
  --green:#8cc63f;
  --green-dark:#6fa82b;
  --text-green:#4a9a12;
  --grey-logo:#8d8d8d;
  --text:#3b3b3b;
  --line:#bdbdbd;
  --sky:#d5eaf7;
  --white:#ffffff;
}
*{margin:0;padding:0;box-sizing:border-box}
html,body{width:1172px;height:1200px;overflow:hidden}
body{position:relative;background:var(--white);font-family:"Arimo",Arial,sans-serif;color:var(--text)}
.abs{position:absolute}
.top-rule{left:0;top:0;width:1172px;height:7px;background:linear-gradient(#8fd2f3,#cbe9f8)}
.header-bg{left:0;top:7px;width:1172px;height:110px;background:var(--white)}
.brand{left:170px;top:43px;display:flex;align-items:center;gap:16px}
.brand-square{width:40px;height:40px;background:var(--gold)}
.brand-name{font-size:44px;letter-spacing:6px;color:var(--grey-logo);font-weight:400;line-height:1}
.share{left:881px;top:25px;display:flex;gap:4px}
.share span{width:13px;height:13px;border-radius:2px;background:#9aa6ae}
.share .count{width:30px;background:#fff;border:1px solid #bbb;font-size:8px;text-align:center;line-height:11px;color:#333}
.callout{right:173px;top:47px;text-align:right}
.callout .phone{font-weight:700;font-size:15.6px;color:var(--green)}
.callout .addr{font-size:12.2px;color:var(--blue);line-height:17px;margin-top:4px}
.nav{left:0;top:117px;width:1172px;height:37px;background:linear-gradient(var(--nav-top),var(--nav-bottom));box-shadow:0 2px 3px rgba(0,0,0,.15)}
.nav ul{position:absolute;left:170px;top:0;list-style:none;display:flex;height:37px}
.nav li{font-weight:700;font-size:15.5px;color:var(--white);line-height:37px;padding:0 16px;position:relative;white-space:nowrap}
.nav li+li::before{content:"";position:absolute;left:0;top:13px;height:13px;border-left:1px solid rgba(255,255,255,.55)}
.nav li.active{background:var(--gold);padding:0 16px 0 15px;width:74px}
.nav li.last::after{content:"";position:absolute;right:-4px;top:13px;height:13px;border-left:1px solid rgba(255,255,255,.55)}
.sky{left:0;top:154px;width:1172px;height:340px;background:linear-gradient(#c5e3f5,#e6f3fb 60%,#f4f9fd)}
.hero{left:170px;top:233px;width:829px;height:241px;border-radius:8px;background:linear-gradient(#f7fbfd,#eef3f6);box-shadow:0 0 3px rgba(0,0,0,.12)}
.hero-title{left:208px;top:262px;font-family:"Oswald",sans-serif;font-weight:500;font-size:21px;line-height:26px;color:var(--blue)}
.hero-title .amp{color:var(--gold)}
.hero-list{left:208px;top:346px;list-style:none;font-size:12.3px;line-height:15px;color:var(--text-green);white-space:nowrap}
.hero-list li::before{content:"→ ";color:var(--gold)}
.btn{display:flex;align-items:center;gap:6px;background:linear-gradient(#9fd255,var(--green-dark));color:var(--white);border:1px solid #8bbd45;padding-left:8px;white-space:nowrap;overflow:hidden}
.btn::before{content:"›";font-size:15px;font-weight:700;line-height:1}
.hero-btn{left:208px;top:418px;width:208px;height:21px;font-size:10.2px}
.video{left:587px;top:189px;width:380px;height:244px;border:3px solid #6f8fa8;background:#fff}
.video .scene{position:absolute;inset:0;background:linear-gradient(110deg,#eef2f4 10%,#c9d3d8 45%,#e6ecef 75%,#ffffff)}
.video .play{position:absolute;left:124px;top:73px;width:128px;height:96px;border-radius:14px;background:rgba(235,235,235,.85);box-shadow:0 1px 4px rgba(0,0,0,.2)}
.arrow{width:23px;height:23px;background:var(--green);border:2px solid #cfe8a8;border-radius:2px}
.dots{left:565px;top:455px;display:flex;gap:2px}
.dots span{width:13px;height:13px;border-radius:50%;background:#9b9b9b}
.dots span:first-child{background:var(--green-dark)}
.panel{background:var(--white);border-radius:6px;box-shadow:0 0 3px rgba(0,0,0,.12);border-bottom:4px solid #cfe5b0}
.main{left:170px;top:483px;width:577px;height:592px}
.side{left:759px;top:483px;width:240px;height:592px}
.section-head{font-family:"Oswald",sans-serif;font-weight:500;font-size:17.5px;color:var(--blue);border-bottom:1px solid var(--line);padding-bottom:1px;line-height:22px;white-space:nowrap}
.photo-frame{left:189px;top:561px;width:213px;height:315px;background:#fff;box-shadow:-3px 3px 6px rgba(0,0,0,.12);padding:6px}
.photo-frame div{width:100%;height:100%;border:1px solid #999;background:linear-gradient(#f4f4f4,#c9d6e3 55%,#7f9fbf)}
.copy{font-size:11.3px;line-height:13.5px;text-align:justify}
.copy p+p{margin-top:13px}
.badge-round{border-radius:50%}
.face-shot{left:194px;top:945px;width:151px;height:86px;background:linear-gradient(90deg,#3b86ae,#8ec3df 60%,#e9eef1)}
.links{left:353px;top:1013px;width:374px;font-size:11.3px;line-height:14px;color:var(--text-green)}
.links a{color:var(--text-green)}
.form-label{font-size:11.8px;color:var(--text)}
.field{background:#fff;border:1px solid #d6d6d6;box-shadow:inset 0 1px 2px rgba(0,0,0,.08)}
.side-btn{width:96px;height:21px;font-size:11px}
.social{left:767px;top:1021px;display:flex;gap:5px}
.social span{width:27px;height:27px;border-radius:3px}
.footer{left:170px;top:1090px;width:829px;height:110px;background:var(--green);border-radius:8px 8px 0 0}
.footer-nav{left:196px;top:1130px;font-size:10.5px;color:var(--white);line-height:17px;white-space:nowrap}
.footer-nav .sep{margin:0 5px}
.footer-brand{left:730px;top:1128px;display:flex;align-items:center;gap:12px}
.footer-brand .brand-square{width:36px;height:36px;background:#fff}
.footer-brand .brand-name{font-size:36px;letter-spacing:5px;color:var(--white)}
</style>
</head>
<body>
<div class="abs top-rule"></div>
<div class="abs header-bg"></div>

<header>
  <div class="abs brand"><span class="brand-square"></span><span class="brand-name">ZENTROL</span></div>
  <div class="abs share"><span></span><span></span><span></span><span></span><span></span><span class="count">3</span></div>
  <div class="abs callout">
    <div class="phone">Call Us Today (212) 555-0184</div>
    <div class="addr">418 Carrow Avenue - Suite 210<br>Brookfield, NY 10290</div>
  </div>
</header>

<nav class="abs nav">
  <ul>
    <li class="active">Home</li><li>Solutions</li><li>Resources</li><li>About</li><li>Why Zentrol</li><li class="last">Contact</li>
  </ul>
</nav>

<div class="abs sky"></div>

<section>
  <div class="abs hero"></div>
  <h1 class="abs hero-title">Internet Marketing <span class="amp">&amp;</span><br>Websites for Medical Practices</h1>
  <ul class="abs hero-list">
    <li>Proven to help grow medical practices — 6,000+ satisfied clients</li>
    <li>Websites, mobile sites, local search and more...</li>
    <li>Fast, easy and affordable</li>
  </ul>
  <div class="abs btn hero-btn">Select Your Specialty to View Samples</div>
  <div class="abs video">
    <div class="scene" role="img" aria-label="Video still of doctors reviewing a computer screen"></div>
    <div class="play"><svg width="128" height="96" viewBox="0 0 128 96"><path d="M46 28 L88 48 L46 68 Z" fill="#111"/></svg></div>
  </div>
  <div class="abs arrow" style="left:162px;top:339px"><svg width="19" height="19" viewBox="0 0 19 19"><path d="M12 3 L6 9.5 L12 16" stroke="#fff" stroke-width="3" fill="none"/></svg></div>
  <div class="abs arrow" style="left:983px;top:339px"><svg width="19" height="19" viewBox="0 0 19 19"><path d="M7 3 L13 9.5 L7 16" stroke="#fff" stroke-width="3" fill="none"/></svg></div>
  <div class="abs dots"><span></span><span></span><span></span></div>
</section>

<main>
  <div class="abs panel main"></div>
  <h2 class="abs section-head" style="left:192px;top:514px;width:536px">Internet Marketing Websites for Medical Practices</h2>
  <div class="abs photo-frame"><div role="img" aria-label="Photo of a doctor in a lab coat reading a patient file"></div></div>
  <div class="abs copy" style="left:420px;top:566px;width:307px">
    <p>Lorem ipsum dolor sit amet, consectetur adipisicing elit, sed do eiusmod tempor incididunt ut labore et dolore magna aliqua. Ut enim ad minim veniam, quis nostrud exercitation ullamco laboris nisi ut aliquip ex ea commodo consequat. Duis aute irure dolor in reprehenderit in voluptate velit esse cillum dolore eu fugiat nulla pariatur. Excepteur sint occaecat cupidatat non proident, sunt in culpa qui officia deserunt mollit anim id est laborum.</p>
    <p>Excepteur sint occaecat cupidatat non proident, sunt in culpa qui officia deserunt mollit anim id est laborum.</p>
    <p>We look forward to welcoming you into our New location!</p>
    <p>Linden Hearing Group, PLLC<br>418 Carrow Avenue - Suite 210<br>Brookfield, NY 10290</p>
  </div>
  <div class="abs badge-round" style="left:422px;top:813px;width:63px;height:63px;background:#ef7d22"></div>
  <div class="abs badge-round" style="left:500px;top:813px;width:63px;height:63px;background:#222"></div>
  <div class="abs" style="left:577px;top:820px;width:108px;height:48px;background:#d7e3e6"></div>

  <h2 class="abs section-head" style="left:192px;top:897px;width:536px">Give Your Practice :: <span style="color:var(--green-dark)">The Exposure it Deserves</span></h2>
  <div class="abs face-shot" role="img" aria-label="Photo of a surgeon in cap and mask"></div>
  <div class="abs copy" style="left:353px;top:944px;width:374px">Lorem ipsum dolor sit amet, consectetur adipisicing elit, sed do eiusmod tempor incididunt ut labore et dolore magna aliqua. Ut enim ad minim veniam, quis nostrud exercitation ullamco laboris nisi ut aliquip ex ea commodo consequat.</div>
  <div class="abs links"><a>ImplantGuide.com</a>, <a>LaserCareHub.com</a>, <a>SurgeryPayPlan.com</a>, <a>ExpectingNotes.com</a>, <a>CosmeticPayPlan.com</a>, <a>ContourRecovery.com</a>, <a>JointImplantInfo.com</a>. <a>[See All Listing Sites]</a></div>
</main>

<aside>
  <div class="abs panel side"></div>
  <h2 class="abs section-head" style="left:768px;top:514px;width:222px">Ask the Experts</h2>
  <div class="abs form-label" style="left:772px;top:555px">Do you have a question for us?</div>
  <div class="abs form-label" style="left:772px;top:584px">Name</div>
  <div class="abs field" style="left:815px;top:581px;width:148px;height:19px"></div>
  <div class="abs form-label" style="left:772px;top:608px">Email</div>
  <div class="abs field" style="left:815px;top:605px;width:148px;height:19px"></div>
  <div class="abs form-label" style="left:772px;top:632px">Phone</div>
  <div class="abs field" style="left:815px;top:629px;width:148px;height:19px"></div>
  <div class="abs form-label" style="left:772px;top:657px">Question</div>
  <div class="abs field" style="left:772px;top:678px;width:197px;height:71px"></div>
  <div class="abs btn side-btn" style="left:773px;top:760px">Ask Now</div>

  <h2 class="abs section-head" style="left:767px;top:819px;width:223px">Newsletter Sign Up</h2>
  <div class="abs form-label" style="left:772px;top:856px;width:218px;line-height:15px">Enter your email address to be added to our mailing list and stay up to date.</div>
  <div class="abs field" style="left:772px;top:892px;width:174px;height:19px"></div>
  <div class="abs btn side-btn" style="left:773px;top:921px">Join List</div>

  <h2 class="abs section-head" style="left:767px;top:980px;width:223px">Stay Social</h2>
  <div class="abs social">
    <span style="background:#3b5a9a"></span><span style="background:#5fc6e8"></span><span style="background:#f08a24"></span><span style="background:#1e78b4"></span><span style="background:#e6e6e6"></span><span style="background:#3a67a8"></span><span style="background:#c9231c"></span>
  </div>
</aside>

<footer>
  <div class="abs footer"></div>
  <div class="abs footer-nav">Home<span class="sep">|</span>Solutions<span class="sep">|</span>Resources<span class="sep">|</span>About<span class="sep">|</span>Why Zentrol<span class="sep">|</span>Contact<br>Copyright © 2012, ZENTROL, All Rights Reserved!</div>
  <div class="abs footer-brand"><span class="brand-square"></span><span class="brand-name">ZENTROL</span></div>
</footer>
</body>
</html>
```